Web Design Project

Website Design Brief

Company Details
1a) Name of Company

BRAMBLECOURT
1) What is the nature of your business?: Briefly describe your products or services:

INDEPENDENT CONTEMPORARY TRADITIONAL ITALIAN RESTAURANT IN THE HEART OF FENWORTH QUAY ALSO CATERING FOR PRIVATE CORPORATE EVENTS AND WEDDING RECEPTIONS

1a) Who is your target market? Who are you hoping to reach with your site?

CITY CORPORATES, LOCAL CORPORATES/BUSINESSES, LOCAL RESIDENTS, VISITORS TO THE DOCK, LOCAL HOTELS

Website Details
1b) Do you have an existing website? If so, what is the URL?
HTTP://WWW.BRAMBLECOURTFOODHALL.COM

2b) IMPORTANT: Please list at least 3 URLs (web addresses) of high quality sites that you like the look of (these do not have to be sites who’s business is similar to yours. It aids us in determining what your design style is.) Please consider layout, colours, navigation, graphics, and typography.

http://www.thewexmoor.co.uk/

http://www.corriveth.co.uk/

http://www.tovirestaurant.com/

http://www.osprelo.co.uk/

3b) What colours or colour schemes would you like?

WHITE, BLACK, SILVER/ALUMINIUM (PLS LOOK AT OUR OUTSIDE CHAIRS)

4b) List the Navigation links for your Site:

5b) What type of look are you trying to achieve? (e.g. clean, high-tech, conservative, warm, flashy, etc.)

SIMPLE ELEGANT CLASSY INFORMATIVE, EASY TO USE, A REFLECTION OF THE BUSINESS ITSELF

6b) Please provide the addresses of competitors' sites, if possible:

Do not contact the client direct - all questions should go through Larkmoor Hospitality - info@larkmoorhospitality.co.uk
Updates

thanks for the designs that I have received so far. I have these general comments:

- please avoid using icons for phones or paperclips etc 
- use dummy text (one design used text from another website) 
- there won't any live social media feeds to the site
the client likes a lot of the designs that this company comes up with: 

i look forward to see some more designs

hi all, 

further to my last update, here are a few more pointers:
- there will be no search facilities - so no "search" box please 
- please just use the images supplied - no stock ones
- use just the page names give (no other pages) 

The client is looking for a simple, elegant design. 

Many thanks 
Neil 

thanks for all the designs. 

I have uploaded another file to the brief which shows some posters that the client particularly likes. Perhaps the homepage could consist of large rectangle made up of a number of boxes - for some introductory text, a large image, mailing list, contact details, Lunch Special etc - just an idea! 
It's clear that the client likes clean lines with square edges. 
I want to be able to pass the designs directly onto the client so can designers avoid adding extra info or page. For example one design has a tab for a "Gift Card" - it will be easier for me if such additions are avoided. 

thanks!                                                                                                                                                                                                                                                                                                                                                                                                    

Thank you for all your designs - please keep them coming! 

hi all,

I am meeting the client tomorrow afternoon so please submit revisions / designs before then. 

Many thanks, 
Neil

Target Market(s)

Business people, upmarket etc

Industry/Entity Type

Business

Requirements
Must have
• - The home page needs a slide show of images as well as:
- a mailing list form - very simple, "Join our mailing list - name, email"
- 3 or 4 sentences of text
- facebook link

```html
<!DOCTYPE html>
<html lang="en">
<head>
<meta charset="utf-8">
<title>Bramblecourt Italian</title>
<link href="https://fonts.googleapis.com/css2?family=Questrial&family=Arimo:wght@400;700&family=Great+Vibes&display=swap" rel="stylesheet">
<style>
:root{
  --page-bg:#f3f3f3;
  --footer-bg:#ececec;
  --accent:#e0461a;
  --ink:#1c1c1c;
  --text:#4a4a4a;
  --muted:#7a7a7a;
  --button:#5e5e5e;
  --rule:#cfcfcf;
  --field:#ffffff;
}
*{margin:0;padding:0;box-sizing:border-box}
html,body{width:1200px;height:972px;overflow:hidden}
body{position:relative;background:var(--page-bg);font-family:"Arimo",Arial,sans-serif;color:var(--text)}
.abs{position:absolute}
.display{font-family:"Questrial",Arial,sans-serif;font-weight:400}

.brand{left:174px;top:38px;font-family:"Questrial",sans-serif;font-size:38px;color:var(--ink);letter-spacing:1px}
.btn{display:block;background:linear-gradient(#6a6a6a,#4f4f4f);color:#fff;font-family:"Questrial",sans-serif;font-size:14px;letter-spacing:1px;text-align:center;line-height:26px;text-decoration:none}
.book-top{left:612px;top:40px;width:130px}
.call{left:756px;top:40px;font-family:"Questrial",sans-serif;font-size:17.5px;color:var(--ink);letter-spacing:.4px;line-height:26px}
.call span{color:var(--accent)}

.nav{left:404px;top:88px;display:flex;list-style:none;font-family:"Questrial",sans-serif;font-size:13px;letter-spacing:.3px}
.nav li{padding:9px 7px;color:#6b6b6b}
.nav li.active{color:var(--accent);background:#fff;border:1px solid #d6d6d6;border-bottom:none;padding:8px 9px 10px}

.hero{left:166px;top:124px;width:868px;height:377px;border:1px solid #fff;box-shadow:0 0 4px rgba(0,0,0,.25);background:linear-gradient(100deg,#3a2a24 0%,#6b3222 30%,#8f5a40 55%,#c9b9ad 75%,#7a4a38 100%)}
.hero-caption{right:0;bottom:0;width:309px;height:75px;background:rgba(90,90,90,.92);color:#fff;text-align:center}
.hero-caption .script{font-family:"Great Vibes",cursive;font-size:32px;line-height:44px;margin-top:4px}
.hero-caption .prices{font-family:"Questrial",sans-serif;font-size:16px}
.hero-caption .sep{color:#999;margin:0 14px}

.feature{left:175px;top:530px;width:263px;height:169px;background:linear-gradient(135deg,#d8d4cf,#b89a6c 45%,#6b7a3a 70%,#e6e2dc)}
.dots{display:flex;gap:2px}
.dots i{width:9px;height:8px;background:#8a8a8a}
.dots i.on{background:var(--accent)}
.feature-dots{left:175px;top:707px}

.welcome-title{left:472px;top:524px;font-size:28px;color:var(--accent)}
.welcome-rule{left:472px;top:563px;width:561px;border-top:1px solid var(--rule)}
.welcome-text{left:472px;top:577px;width:553px;height:114px;overflow:hidden;font-size:11.2px;line-height:16.2px;text-align:justify;color:#555}
.book-main{left:472px;top:708px;width:131px}

.footer{left:0;top:768px;width:1200px;height:204px;background:var(--footer-bg);border-top:1px solid #dcdcdc}
.foot-title{font-family:"Questrial",sans-serif;font-size:21px;color:var(--accent);font-weight:400}
.touch-title{left:174px;top:784px}
.address{left:175px;top:818px;font-size:12.5px;line-height:16.5px;color:var(--muted);font-style:normal}
.contact{left:485px;top:818px;font-size:12.5px;line-height:16.5px;color:var(--muted)}
.contact a{color:var(--accent);text-decoration:none}

.mailing{left:485px;top:872px;width:300px;font-size:12px;color:#3a3a3a}
.mailing-label{font-weight:700;margin-bottom:5px;display:block}
.mailing-row{display:flex;gap:4px}
.mailing-field{height:20px;border:1px solid #cfcfcf;background:var(--field);font:11px "Arimo",sans-serif;color:#999;padding:0 5px;line-height:18px}
.field-name{width:100px}
.field-email{width:130px}
.mailing-submit{width:52px;height:20px;line-height:20px;font-size:11px}

.news-title{left:810px;top:788px}
.news{left:811px;top:818px;width:220px;font-size:12.5px;color:var(--muted)}
.news h3{font-size:12.5px;color:#3a3a3a;margin-bottom:6px}
.news p{line-height:13px;margin-bottom:10px}
.news .more{color:var(--accent);font-weight:700}
.news-dots{left:812px;top:894px}
.foot-rule{left:175px;top:925px;width:850px;border-top:1px solid #d4d4d4}
.foot-links{left:172px;top:939px;display:flex;gap:15px;list-style:none;font-size:12.5px;color:var(--muted)}
.copyright{right:175px;top:939px;font-size:12.5px;color:var(--muted)}
</style>
</head>
<body>
<header>
  <div class="abs brand">Bramblecourt</div>
  <a class="abs btn book-top" href="#">BOOK EVENT</a>
  <div class="abs call">OR CALL US ON: <span>020 7946 0318</span></div>
  <ul class="abs nav">
    <li>WELCOME</li><li>OUR RESTAURANT</li><li class="active">OUR MENU</li><li>GALLERY</li><li>EVENTS</li><li>RESERVATIONS</li><li>CONTACT</li>
  </ul>
</header>

<section class="abs hero" role="img" aria-label="Restaurant lounge with white leather sofas, a tall lamp and string curtains before city windows">
  <div class="abs hero-caption">
    <div class="script">Lunch Set Menu</div>
    <div class="prices">2 Courses £15<span class="sep">|</span>3 Courses £20</div>
  </div>
</section>

<main>
  <div class="abs feature" role="img" aria-label="Plated dish of grilled vegetables, salad leaves and raspberries"></div>
  <div class="abs dots feature-dots"><i></i><i></i><i class="on"></i></div>
  <h1 class="abs display welcome-title">Welcome To Bramblecourt</h1>
  <div class="abs welcome-rule"></div>
  <p class="abs welcome-text">Lorem ipsum dolor sit amet, consectetuer adipiscing elit. Aenean commodo ligula eget dolor. Aenean massa. Cum sociis natoque penatibus et magnis dis parturient montes, nascetur ridiculus mus. Donec quam felis, ultricies nec, pellentesque eu, pretium quis, sem. Nulla consequat massa quis enim. Donec pede justo, fringilla vel, aliquet nec, vulputate eget, arcu. In enim justo, rhoncus ut, imperdiet a, venenatis vitae, justo. Nullam dictum felis eu pede mollis pretium. Integer tincidunt. Cras dapibus. Vivamus elementum semper nisi. Aenean vulputate eleifend tellus. Aenean leo ligula, porttitor eu, consequat vitae, eleifend ac, enim. Aliquam lorem ante, dapibus in, viverra quis, feugiat a, tellus. Phasellus viverra nulla ut metus</p>
  <a class="abs btn book-main" href="#">BOOK EVENT</a>
</main>

<footer class="abs footer"></footer>
<h2 class="abs foot-title touch-title">Get in touch...</h2>
<address class="abs address">The Bramblecourt Italian 50 Fenworth Quay<br>Way, City of London,<br>London<br>E1W 9QX;</address>
<div class="abs contact">Tel: 020 7946 0318<br>Email Us: <a href="#">info@bramblecourtitalian.com</a><br>Follow Us: <a href="#">Our social page</a></div>
<form class="abs mailing">
  <span class="mailing-label">Join our mailing list</span>
  <div class="mailing-row">
    <div class="mailing-field field-name">Name</div>
    <div class="mailing-field field-email">Email</div>
    <a class="btn mailing-submit" href="#">JOIN</a>
  </div>
</form>
<h2 class="abs foot-title news-title">News</h2>
<div class="abs news">
  <h3>Basil Wins Diner Platinum Award!</h3>
  <p>Basil prides itself on providing our guests with a tantalizing ...</p>
  <div><span class="more">Read More</span> | May 27th, 2011</div>
</div>
<div class="abs dots news-dots"><i></i><i></i><i class="on"></i></div>
<div class="abs foot-rule"></div>
<ul class="abs foot-links">
  <li>Welcome</li><li>Our Restaurant</li><li>Our Menu</li><li>Gallery</li><li>Events</li><li>Reservations</li><li>Contact</li>
</ul>
<div class="abs copyright">Copyright © Bramblecourt The Bramblecourt Italian</div>
</body>
</html>
```